Pinecrest Premier Motors *

Professional business cards for our auto wholesale dealership.

Target Market(s)

New and used cars sales managers and middle class to higher end private party buyers.

Industry/Entity Type

Automotive

Contact Information for Business Card

Pinecrest Premier Motors
Marcus T Holloran
Owner
(555) 014-3862
pineprem@mailvista.example
Dealer Lic # 48265

Logo Text

Pinecrest Premier Motors, Pine Prem Motors, PPM, etc

Font styles to use
Serif
Sans Serif

Colors

Designer to choose colors to be used in the design.

Requirements
Must have
• A professional, but not pretentious, look
Nice to have
• It might be nice to see "PPM" in a shape form i.e. circle, triangle, etc in the corner or background somehwere
Should not have
• bright "girly" colors

```html
<!DOCTYPE html>
<html lang="en">
<head>
<meta charset="utf-8">
<title>Pinecrest Premier Motors – Business Card</title>
<link rel="stylesheet" href="https://fonts.googleapis.com/css2?family=Lato:wght@400;700;900&display=swap">
<style>
  :root {
    --backdrop: #3a3a3a;
    --card: #0b0b0b;
    --silver: #d4d6d9;
    --silver-muted: #9a9da2;
    --white: #f4f4f4;
    --divider: #5a5a5a;
  }
  * { box-sizing: border-box; margin: 0; padding: 0; }
  html, body { width: 1200px; height: 1189px; overflow: hidden; }
  body {
    background: var(--backdrop);
    font-family: "Lato", sans-serif;
    position: relative;
  }
  .card {
    position: absolute;
    left: 170px;
    width: 860px;
    height: 490px;
    background: var(--card);
    border-radius: 34px;
    overflow: hidden;
  }
  .card--front { top: 50px; }
  .card--back { top: 630px; }

  .brand {
    display: flex;
    flex-direction: column;
    align-items: center;
    gap: 22px;
  }
  .brand__seal {
    width: 150px; height: 150px;
    border-radius: 50%;
    border: 8px solid var(--silver);
  }
  .brand__name {
    color: var(--silver);
    font-weight: 900;
    font-size: 30px;
    letter-spacing: 3px;
    text-transform: uppercase;
    text-align: center;
    line-height: 1.25;
  }
  .card--front .brand {
    position: absolute; left: 0; right: 0; top: 105px;
  }

  .card--back .brand {
    position: absolute; left: 40px; width: 340px; top: 110px;
  }
  .card--back .brand__seal { width: 170px; height: 170px; }
  .card--back .brand__name { font-size: 27px; }

  .divider {
    position: absolute;
    left: 410px; top: 95px;
    width: 1px; height: 300px;
    background: var(--divider);
  }
  .contact {
    position: absolute;
    left: 455px; top: 115px;
    color: var(--white);
  }
  .contact__name {
    font-weight: 900;
    font-size: 29px;
    letter-spacing: 1px;
    text-transform: uppercase;
  }
  .contact__role {
    font-size: 21px;
    color: var(--silver-muted);
    margin-top: 2px;
    margin-left: 10px;
  }
  .contact__list { list-style: none; margin-top: 42px; font-size: 22px; }
  .contact__item { display: flex; align-items: center; gap: 10px; height: 36px; }
  .contact__icon { width: 26px; height: 26px; flex: none; }
  .contact__item--plain { padding-left: 36px; }
</style>
</head>
<body>
  <section class="card card--front">
    <div class="brand">
      <div class="brand__seal"></div>
      <div class="brand__name">Pinecrest<br>Premier Motors</div>
    </div>
  </section>

  <section class="card card--back">
    <div class="brand">
      <div class="brand__seal"></div>
      <div class="brand__name">Pinecrest<br>Premier Motors</div>
    </div>
    <div class="divider"></div>
    <div class="contact">
      <h1 class="contact__name">Marcus T Holloran</h1>
      <p class="contact__role">Owner</p>
      <ul class="contact__list">
        <li class="contact__item">
          <svg class="contact__icon" viewBox="0 0 26 26" aria-hidden="true">
            <circle cx="13" cy="13" r="12" fill="none" stroke="#f4f4f4" stroke-width="1.5"/>
            <path d="M9 7.5c1-.6 1.8 0 2.3 1l.8 1.7c.3.7 0 1.3-.6 1.7l-.6.4c.6 1.6 1.6 2.8 3 3.7l.5-.5c.5-.5 1.2-.6 1.8-.2l1.5 1c.8.6.9 1.4.2 2.2-1.4 1.4-3.5 1-5.6-.7-2.2-1.8-3.6-4.2-4-6.4-.2-1.4.2-2.5.7-2.9z" fill="#f4f4f4"/>
          </svg>
          <span>(555) 014-3862</span>
        </li>
        <li class="contact__item">
          <svg class="contact__icon" viewBox="0 0 26 26" aria-hidden="true">
            <circle cx="13" cy="13" r="12" fill="none" stroke="#f4f4f4" stroke-width="1.5"/>
            <rect x="7" y="9" width="12" height="8.5" fill="none" stroke="#f4f4f4" stroke-width="1.4"/>
            <path d="M7 9l6 5 6-5" fill="none" stroke="#f4f4f4" stroke-width="1.4"/>
          </svg>
          <span>pineprem@mailvista.example</span>
        </li>
        <li class="contact__item contact__item--plain">Dealer Lic # 48265</li>
      </ul>
    </div>
  </section>
</body>
</html>
```